Harlow Ridge Growers and Nursery needs a business street sign.

I have three businesses located at the same address: The Harlow Ridge Growers & Nursery, The Bramble Nook, and The Quarry Commons. I am looking for a 4’ x 8’ street sign to represent all three businesses as one retail experience. It needs to be eye catching yet simple enough that people can fully read it while driving by. I have logos for the greenhouse and village however I do not have anything for The Bramble Nook. I’m looking for some type of font that’s similar or in between the two attached logos for The Bramble Nook.

• Horizontal Sign, Eye catching, yet simple design so people see it while driving by.
• Horizontal Sign
• I’m open to the design being both vertical and horizontal. Please provide both options

```html
<!DOCTYPE html>
<html lang="en">
<head>
<meta charset="utf-8">
<title>Harlow Ridge Growers and Nursery – Street Sign</title>
<link rel="stylesheet" href="https://fonts.googleapis.com/css2?family=Fredoka:wght@600&display=swap">
<style>
  :root {
    --backdrop: #8a8a8a;
    --wood-light: #f8e4cf;
    --wood-mid: #f1d4b6;
    --frame-tan: #e6c39c;
    --edge-white: #ffffff;
    --panel-white: #ffffff;
    --garden-green: #1f6b3d;
    --nook-green: #7db343;
    --nook-bloom: #c65ad9;
    --commons-red: #8e2b20;
  }
  html, body {
    margin: 0;
    padding: 0;
    overflow: hidden;
    background: var(--backdrop);
  }
  .canvas {
    width: 1200px;
    height: 600px;
    background: var(--backdrop);
    overflow: hidden;
  }
  .sign {
    display: block;
    width: 1200px;
    height: 600px;
  }
  .sign__board { fill: url(#woodTone); stroke: var(--edge-white); stroke-width: 4; }
  .sign__inner-edge { fill: none; stroke: var(--frame-tan); stroke-width: 5; }
  .panel__rim { fill: var(--frame-tan); }
  .panel__face { fill: var(--panel-white); }
  .business-name {
    font-family: "Fredoka", "Trebuchet MS", sans-serif;
    font-weight: 600;
    text-anchor: middle;
  }
  .business-name--growers { fill: var(--garden-green); }
  .business-name--nook { fill: var(--nook-green); }
  .business-name--commons { fill: var(--commons-red); }
  .nook-dot { fill: var(--nook-bloom); }
</style>
</head>
<body>
<main class="canvas">
  <svg class="sign" viewBox="0 0 1426 713" role="img" aria-label="Street sign for The Harlow Ridge Growers and Nursery, The Bramble Nook and The Quarry Commons">
    <defs>
      <linearGradient id="woodTone" x1="0" y1="0" x2="0" y2="1">
        <stop offset="0" stop-color="var(--wood-light)"/>
        <stop offset="1" stop-color="var(--wood-mid)"/>
      </linearGradient>
      <filter id="boardShadow" x="-10%" y="-10%" width="120%" height="130%">
        <feDropShadow dx="0" dy="8" stdDeviation="8" flood-color="#000" flood-opacity="0.35"/>
      </filter>
    </defs>

    <g class="sign__body" filter="url(#boardShadow)">
      <path class="sign__board" d="
        M122 196
        C250 190 360 170 420 112
        C470 70 560 50 713 48
        C866 50 956 70 1006 112
        C1066 170 1176 190 1304 196
        C1288 290 1288 430 1304 524
        C1176 530 1066 550 1006 600
        C956 642 866 664 713 666
        C560 664 470 642 420 600
        C360 550 250 530 122 524
        C138 430 138 290 122 196 Z"/>
    </g>
    <path class="sign__inner-edge" d="
      M146 214
      C265 208 372 188 432 132
      C482 90 568 70 713 68
      C858 70 944 90 994 132
      C1054 188 1161 208 1280 214
      C1266 300 1266 420 1280 506
      C1161 512 1054 532 994 580
      C944 624 858 644 713 646
      C568 644 482 624 432 580
      C372 532 265 512 146 506
      C160 420 160 300 146 214 Z"/>

    <g class="panels">
      <ellipse class="panel__rim" cx="355" cy="370" rx="192" ry="176"/>
      <ellipse class="panel__rim" cx="713" cy="352" rx="222" ry="222"/>
      <ellipse class="panel__rim" cx="1070" cy="370" rx="196" ry="176"/>
      <ellipse class="panel__face" cx="355" cy="370" rx="180" ry="164"/>
      <ellipse class="panel__face" cx="713" cy="352" rx="210" ry="210"/>
      <ellipse class="panel__face" cx="1070" cy="370" rx="184" ry="164"/>
    </g>

    <g class="business business--growers">
      <text class="business-name business-name--growers" x="365" y="362" font-size="52">Harlow Ridge</text>
      <text class="business-name business-name--growers" x="365" y="410" font-size="26">Growers &amp; Nursery</text>
    </g>

    <g class="business business--nook">
      <circle class="nook-dot" cx="713" cy="290" r="26"/>
      <text class="business-name business-name--nook" x="713" y="385" font-size="70">Bramble</text>
      <text class="business-name business-name--nook" x="713" y="450" font-size="62">Nook</text>
    </g>

    <g class="business business--commons">
      <text class="business-name business-name--commons" x="1080" y="360" font-size="62">Quarry</text>
      <text class="business-name business-name--commons" x="1080" y="412" font-size="44">Commons</text>
    </g>
  </svg>
</main>
</body>
</html>
```